Cobalt Ridge Mini Storage - Ad for half Page

Need half page ad for a publication.
would also like to be able to use in the future
self storage facility - 3 locations, the third opening soon
do not like real busy projects...i have a logo but willing to tweak if needed

```html
<!DOCTYPE html>
<html lang="en">
<head>
<meta charset="utf-8">
<title>Cobalt Ridge Mini Storage – Half Page Ad</title>
<link rel="stylesheet" href="https://fonts.googleapis.com/css2?family=Libre+Baskerville:wght@400;700&display=swap">
<style>
  :root {
    --page-bg: #444444;
    --brown-dark: #5a2a08;
    --brown-text: #5c2a0e;
    --gold: #a0651a;
    --gold-light: #e6b43a;
    --ribbon: #c98a45;
    --white: #ffffff;
    --silver-edge: #c4c4c4;
  }
  html, body {
    margin: 0;
    padding: 0;
    width: 900px;
    height: 1200px;
    overflow: hidden;
    background: var(--page-bg);
    font-family: "Libre Baskerville", Georgia, serif;
  }
  .ad {
    position: absolute;
    left: 102px;
    width: 696px;
    height: 464px;
  }
  .ad--white { top: 84px; }
  .ad--silver { top: 632px; }

  .ad__face {
    position: absolute;
    inset: 0 0 28px 0;
    background: var(--white);
  }
  .ad--silver .ad__face {
    background: linear-gradient(90deg, var(--silver-edge) 0%, #f4f4f4 40%, #f4f4f4 60%, var(--silver-edge) 100%);
  }
  .ad__band {
    position: absolute;
    left: 0; right: 0;
    top: 436px;
    height: 8px;
    background: var(--brown-dark);
  }
  .ad__tab {
    position: absolute;
    left: 130px;
    top: 426px;
    width: 472px;
    height: 38px;
    border-radius: 19px;
    background: linear-gradient(180deg, #b07325 0%, var(--gold) 60%, #8a5512 100%);
  }
  .ad__headline {
    position: absolute;
    top: 28px;
    left: 0; right: 0;
    margin: 0;
    text-align: center;
    font-size: 35px;
    font-weight: 400;
    letter-spacing: 0.5px;
    color: var(--brown-text);
  }
  .ad__headline .accent { color: var(--gold); }

  .ad__panel {
    position: absolute;
    left: 149px;
    top: 119px;
    width: 380px;
    height: 178px;
    border-radius: 6px;
    background: var(--brown-dark);
  }
  .ad__art {
    position: absolute;
    inset: 0;
    width: 696px;
    height: 464px;
  }
  .ad__message {
    position: absolute;
    left: 190px;
    top: 146px;
    margin: 0;
    color: var(--white);
    font-weight: 400;
    line-height: 1;
  }
  .ad__message span { display: block; }
  .ad__message .line-1 { font-size: 35px; }
  .ad__message .line-2 { font-size: 40px; margin-top: 6px; }
  .ad__message .line-3 { font-size: 47px; margin-top: 4px; }

  .ad__brand {
    position: absolute;
    left: 206px;
    top: 344px;
    display: flex;
    align-items: center;
    gap: 12px;
  }
  .ad__brand-mark {
    width: 58px;
    height: 58px;
    background: var(--ribbon);
  }
  .ad__brand-name {
    margin: 0;
    font-size: 24px;
    font-weight: 700;
    line-height: 1.15;
    color: var(--brown-text);
  }
</style>
</head>
<body>

<section class="ad ad--white">
  <div class="ad__tab"></div>
  <div class="ad__face"></div>
  <div class="ad__band"></div>
  <h1 class="ad__headline">SELF STORAGE <span class="accent">FACILITY</span></h1>
  <div class="ad__panel"></div>
  <svg class="ad__art" viewBox="0 0 696 464" aria-hidden="true">
    <defs>
      <linearGradient id="frameGold1" x1="0" y1="0" x2="1" y2="1">
        <stop offset="0" stop-color="#e6b43a"/>
        <stop offset="1" stop-color="#a0651a"/>
      </linearGradient>
    </defs>
    <polygon points="194,93 555,137 502,319 122,276" fill="none" stroke="url(#frameGold1)" stroke-width="3"/>
    <polygon points="470,230 643,230 626,248.5 643,267 470,267" fill="#c98a45"/>
    <text x="560" y="259" text-anchor="middle" fill="#ffffff" font-family="Libre Baskerville, Georgia, serif" font-size="30">soon</text>
  </svg>
  <p class="ad__message">
    <span class="line-1">3 LOCATIONS</span>
    <span class="line-2">THE THIRD</span>
    <span class="line-3">OPENING</span>
  </p>
  <div class="ad__brand">
    <div class="ad__brand-mark"></div>
    <p class="ad__brand-name">Cobalt Ridge<br>Mini Storage</p>
  </div>
</section>

<section class="ad ad--silver">
  <div class="ad__tab"></div>
  <div class="ad__face"></div>
  <div class="ad__band"></div>
  <h1 class="ad__headline">SELF STORAGE <span class="accent">FACILITY</span></h1>
  <div class="ad__panel"></div>
  <svg class="ad__art" viewBox="0 0 696 464" aria-hidden="true">
    <defs>
      <linearGradient id="frameGold2" x1="0" y1="0" x2="1" y2="1">
        <stop offset="0" stop-color="#e6b43a"/>
        <stop offset="1" stop-color="#a0651a"/>
      </linearGradient>
    </defs>
    <polygon points="194,93 555,137 502,319 122,276" fill="none" stroke="url(#frameGold2)" stroke-width="3"/>
    <polygon points="470,230 643,230 626,248.5 643,267 470,267" fill="#c98a45"/>
    <text x="560" y="259" text-anchor="middle" fill="#ffffff" font-family="Libre Baskerville, Georgia, serif" font-size="30">soon</text>
  </svg>
  <p class="ad__message">
    <span class="line-1">3 LOCATIONS</span>
    <span class="line-2">THE THIRD</span>
    <span class="line-3">OPENING</span>
  </p>
  <div class="ad__brand">
    <div class="ad__brand-mark"></div>
    <p class="ad__brand-name">Cobalt Ridge<br>Mini Storage</p>
  </div>
</section>

</body>
</html>
```